Mortgage Broking boutique Business

I’m wanting a revamped look to my existing business card design. I do like the black and silver but happy to have other colours introduced based on your creation. I’ve attached a copy of my current card so you can have a starting point updated details noted brloe. I deal with high net worth individuals so need my card to be sophisticated, classy that gives off a classy vibe

Target Market(s)

High net worth, wealthy

Industry/Entity Type

Mortgage Brokerage

Contact Information for Business Card

Job title: Finance Executive
Phone: +61 7 3287 4419
Mobile: 0471 352 608
Email: marcus@quillbrookcapital.com.au
Web: www.quillbrookcapital.com.au
Address: level 36 Tindale Court, 58 Harwick St Brisbane QLD 4000

Font styles to use
Other font styles liked:
• Helvetica

Colors

Designer to choose colors to be used in the design.

Requirements
Must have
• Use my existing card design as a starting point

```html
<!DOCTYPE html>
<html lang="en">
<head>
<meta charset="utf-8">
<title>Quillbrook Capital – Business Card</title>
<link rel="stylesheet" href="https://fonts.googleapis.com/css2?family=Didact+Gothic&family=Montserrat:wght@500;600&display=swap">
<style>
  :root {
    --backdrop: #181818;
    --card: #1f1f1f;
    --silver: #c4c4c4;
    --silver-soft: #b5b5b5;
  }
  * { margin: 0; padding: 0; box-sizing: border-box; }
  html, body {
    width: 1200px; height: 1200px; overflow: hidden;
    background: var(--backdrop);
  }
  .canvas { position: relative; width: 1200px; height: 1200px; }
  .card {
    position: absolute; top: 228px; width: 424px; height: 744px;
    background: var(--card);
    color: var(--silver);
    font-family: "Didact Gothic", "Century Gothic", sans-serif;
    text-align: center;
  }
  .card--front { left: 136px; }
  .card--back { left: 640px; }
  .brand { position: absolute; left: 0; right: 0; }
  .card--front .brand { top: 40px; }
  .card--back .brand { top: 240px; }
  .brand__square {
    display: block; width: 150px; height: 150px; margin: 0 auto 30px;
    background: var(--silver);
  }
  .brand__name {
    font-family: "Montserrat", Helvetica, Arial, sans-serif;
    font-weight: 500; font-size: 31px; line-height: 44px;
    letter-spacing: 3px; color: var(--silver);
  }
  .person { position: absolute; top: 392px; left: 0; right: 0; }
  .person__name {
    font-family: "Montserrat", Helvetica, Arial, sans-serif;
    font-weight: 600; font-size: 26px; letter-spacing: 1px; line-height: 32px;
  }
  .person__title { font-size: 23px; line-height: 30px; color: var(--silver-soft); }
  .details { position: absolute; left: 0; right: 0; font-size: 19px; line-height: 28px; color: var(--silver-soft); }
  .details--address { top: 516px; }
  .details--phones { top: 604px; letter-spacing: 0.5px; }
  .details--email { top: 682px; font-size: 20px; }
  .details--web { top: 682px; font-size: 20px; letter-spacing: 0.5px; }
</style>
</head>
<body>
<main class="canvas">
  <section class="card card--front" aria-label="Card front">
    <div class="brand">
      <span class="brand__square"></span>
      <p class="brand__name">QUILLBROOK<br>CAPITAL</p>
    </div>
    <div class="person">
      <p class="person__name">MARCUS WEXLEY</p>
      <p class="person__title">Finance Executive</p>
    </div>
    <p class="details details--address">level 36 Tindale Court,<br>58 Harwick St Brisbane QLD 4000</p>
    <p class="details details--phones">P : +61 7 3287 4419<br>M : 0471 352 608</p>
    <p class="details details--email">marcus@quillbrookcapital.com.au</p>
  </section>
  <section class="card card--back" aria-label="Card back">
    <div class="brand">
      <span class="brand__square"></span>
      <p class="brand__name">QUILLBROOK<br>CAPITAL</p>
    </div>
    <p class="details details--web">www.quillbrookcapital.com.au</p>
  </section>
</main>
</body>
</html>
```